Brookvane Holdings Ltd - Logo and Business Card

Create a logo and business card design for our new company.

Canadian private investment company with holdings in Saskatchewan Oil and real-estate.

Target Market(s)

Investors

Industry/Entity Type

Finance

Contact Information for Business Card

Logo
Name - Dalton Pryce
Position - President
Phone - 306.482.7159
Website - www.brookvaneholdings.ca

Logo Text

Today. Tomorrow. Together. (Tag Line)

Colors

Designer to choose colors to be used in the design.

Requirements
Must have
• Logo Must Have - Type Font only
• Must be modern, professional and stand out from the crowd.
Nice to have
• Don't have any, blank slate.

```html
<!DOCTYPE html>
<html lang="en">
<head>
<meta charset="utf-8">
<title>Brookvane Holdings Ltd – Business Card</title>
<link rel="stylesheet" href="https://fonts.googleapis.com/css2?family=Libre+Baskerville:wght@700&family=Open+Sans:wght@400;600&display=swap">
<style>
  :root {
    --stage: #2b2b2d;
    --card: #121317;
    --red: #e0202a;
    --grey: #b9b9bb;
    --text-light: #e6e6e6;
    --divider: #5b5c60;
    --band-text: #3a0a0c;
  }
  * { box-sizing: border-box; margin: 0; padding: 0; }
  html, body { width: 1200px; height: 880px; overflow: hidden; }
  body { background: var(--stage); position: relative; font-family: "Open Sans", sans-serif; }

  .card {
    position: absolute;
    width: 620px;
    height: 354px;
    background: var(--card);
    border-radius: 18px;
    overflow: hidden;
    box-shadow: 0 14px 30px rgba(0,0,0,.45);
  }
  .card--front { left: 80px; top: 70px; }
  .card--back  { left: 500px; top: 456px; }

  /* Front */
  .wordmark {
    position: absolute;
    inset: 0;
    display: flex;
    align-items: center;
    justify-content: center;
    gap: 14px;
  }
  .wordmark__square { width: 18px; height: 18px; background: var(--red); flex: none; }
  .wordmark__name {
    font-family: "Libre Baskerville", serif;
    font-weight: 700;
    font-size: 30px;
    color: var(--red);
    letter-spacing: .5px;
    white-space: nowrap;
  }

  /* Back */
  .back__brand {
    position: absolute;
    left: 0; top: 40px;
    width: 258px; height: 250px;
    padding: 0 18px;
    display: flex; align-items: center; justify-content: center;
    gap: 8px;
  }
  .back__brand .wordmark__square { width: 11px; height: 11px; }
  .back__brand .wordmark__name { font-size: 14px; letter-spacing: 0; }

  .back__divider {
    position: absolute;
    left: 258px; top: 90px;
    width: 1px; height: 150px;
    background: var(--divider);
  }
  .person { position: absolute; left: 300px; top: 78px; }
  .person__name {
    font-family: "Libre Baskerville", serif;
    font-weight: 700;
    font-size: 25px;
    color: var(--red);
  }
  .person__role {
    font-weight: 600;
    font-size: 15px;
    color: var(--text-light);
    margin-top: 2px;
    padding-left: 10px;
  }
  .contacts { position: absolute; left: 330px; top: 178px; list-style: none; }
  .contacts__item {
    display: flex; align-items: center; gap: 10px;
    font-size: 15px; color: var(--text-light);
    margin-bottom: 8px;
  }
  .contacts__icon {
    width: 20px; height: 20px; background: var(--red);
    display: flex; align-items: center; justify-content: center;
  }
  .stripe {
    position: absolute; left: 0; right: 0;
    bottom: 54px; height: 9px; background: var(--grey);
  }
  .band {
    position: absolute; left: 0; right: 0; bottom: 0;
    height: 54px; background: var(--red);
    display: flex; align-items: center; justify-content: center;
    font-size: 15px; color: var(--band-text); letter-spacing: .3px;
  }
</style>
</head>
<body>

  <section class="card card--front" aria-label="Card front">
    <div class="wordmark">
      <span class="wordmark__square"></span>
      <span class="wordmark__name">Brookvane Holdings Ltd</span>
    </div>
  </section>

  <section class="card card--back" aria-label="Card back">
    <div class="back__brand">
      <span class="wordmark__square"></span>
      <span class="wordmark__name">Brookvane Holdings Ltd</span>
    </div>
    <div class="back__divider"></div>

    <div class="person">
      <p class="person__name">Dalton Pryce</p>
      <p class="person__role">President</p>
    </div>

    <ul class="contacts">
      <li class="contacts__item">
        <span class="contacts__icon">
          <svg width="13" height="13" viewBox="0 0 24 24" aria-hidden="true">
            <path fill="#fff" d="M6.6 10.8a15.1 15.1 0 0 0 6.6 6.6l2.2-2.2c.3-.3.7-.4 1-.2 1.1.4 2.3.6 3.6.6.6 0 1 .4 1 1V20c0 .6-.4 1-1 1A17 17 0 0 1 3 4c0-.6.4-1 1-1h3.5c.6 0 1 .4 1 1 0 1.3.2 2.5.6 3.6.1.3 0 .7-.2 1z"/>
          </svg>
        </span>
        306.482.7159
      </li>
      <li class="contacts__item">
        <span class="contacts__icon">
          <svg width="13" height="13" viewBox="0 0 24 24" aria-hidden="true">
            <rect x="2" y="5" width="20" height="14" fill="none" stroke="#fff" stroke-width="2"/>
            <path d="M2 5l10 8 10-8" fill="none" stroke="#fff" stroke-width="2"/>
          </svg>
        </span>
        info@brookvaneholdings.ca
      </li>
    </ul>

    <div class="stripe"></div>
    <div class="band">www.brookvaneholdings.ca</div>
  </section>

</body>
</html>
```